Coastal Rubdown Oil Co. needs a new label.

This massage oil has been in Australia for over 20 years and needs a new label for its plastic 250ml bottles. The current label (8cm x 8cm) looks old fashioned and so we are looking for something that reflects freedom, relaxation, inspiration. The product is made from sweet almond oil and has different essential oils used to give unique smells. I have seen some lovely abstract vector images. I think we need a clean straight look with bright colours. There are currently six variations to the product. "Weary and Worn Heads, Achy and Spent Frames, Couples Mix, Heather Soak Oil, Unwinding Mix, Uplift Mix" Different coloured labels have been used for each of the blends. I have included photos of existing bottles plus some ideas for the labels.

I would like to use the same font on the name of the brand Bramblewick Acres. If we change the font it may be difficult for existing customers to find our product.

Also just under the name Bramblewick Acres I would like to insert a type of logo (can be the shape of a tear drop or round circle) to say:

Massage Oil
Since 1970

The size of the label is 8cm x 12 cm for the front and the same size for the back of the label.
Updates

Coastal Rubdown oil Company has posted on the brief some images from Pixelvault plus two photos of the original bottles. I am looking for a new design which is bright in colour, fun and funky. I am not thinking along the lines of the traditional Herb and trees look. I think the original label is too busy and the colours overpower the label. The other point I think that is important is that the product has been around since 1970. If there is room I think a round logo which says: Massage Oil Since 1970 I am hoping that we can fit this information on the label Looking forward to seeing all the designs come thru. So far I have only had two designs come thru. Speak soon from hot sunny Australia. maree

Thank you to everyone who has already posted designs for our Massage Label. I have now edited the brief to include some more ideas on how to make this design the Best! I will email back to you straight away ideas and thoughts on your designs. Remember I live in Australia and can be either 10hrs in front or behind your time.

Reason: Due to busy lives and commitments over the next few days I feel that an extension will benefit all involved. Thank you to everyone who has submitted designs and working with me to create something beautiful. maree

Hello from Australia all the designers who have submitted some wonderful designs over the past two weeks. We are now entering the final three days of the competition. Thank you to everyone who has worked so hard to try and create the perfect label for my massage oil bottle. All of you have done a fantastic job. This has made the decision hard to make. Thank you to everyone. Please submit all your last minute designs soon. kind regards maree Australia

Target Market(s)

The type of person purchasing a massage oil blend will buy from a health food shop, pharmacy or from an on-line store. I believe they are wanting something bright that clearly communicates that that it is a massage oil.

Industry/Entity Type

Massage

Font styles to use
Script

Requirements
Must have
• Different colour for each massage oil blend.
Need same font for the name Bramblewick Acres. (script font or similar)

Abstract design please.
Nice to have
• A logo under the name Bramblewick Acres

Tear Drop or circle design that says:

Massage Oil
Since 1970

also we would like an outline for the back label. (see photo attached)

BACK LABEL information

A unique blend of essential oils in a fine light base.

Contains:

vegetable oil extract of nettle, sweet almond oil, ethanol, essential oils of lavender, lemongrass, orange & ylang ylang and vitamin E.

How to Use:

Shake well warm bottle in warm water if very cold.
Lovingly massage the body from head to toe.
Not for medicinal use.

Bramblewick Acres
Hollin WA 6099
Phone: (08) 9555 0142

(LEAVE ROOM FOR BARCODE)
Should not have
• Too busy design or old fashioned design.
No dull colours.

```html
<!DOCTYPE html>
<html lang="en">
<head>
<meta charset="utf-8">
<title>Bramblewick Acres – Unwinding Mix Label</title>
<link rel="stylesheet" href="https://fonts.googleapis.com/css2?family=Great+Vibes&family=Tinos:wght@700&family=Arimo:wght@400;700&display=swap">
<style>
  :root {
    --paper: #ffffff;
    --silver-light: #f4f4f4;
    --silver-mid: #d9d9d9;
    --silver-dark: #bdbdbd;
    --badge-blue: #1a9ee0;
    --wave-blue: #0a96d8;
    --navy: #0b2a78;
    --ink: #111111;
    --dot-green: #1a9a3a;
    --dot-blue: #1a9ee0;
    --dot-red: #e0231c;
    --dot-orange: #f08a1c;
    --dot-yellow: #ffee00;
  }
  * { margin: 0; padding: 0; box-sizing: border-box; }
  html, body { width: 812px; height: 1200px; overflow: hidden; background: var(--paper); }
  .label {
    position: relative;
    width: 812px;
    height: 1200px;
    overflow: hidden;
    background: var(--paper);
    font-family: "Arimo", Arial, sans-serif;
  }
  .label__art { position: absolute; inset: 0; }
  .badge-text {
    position: absolute;
    left: 250px;
    width: 300px;
    top: 262px;
    text-align: center;
    font-family: "Tinos", "Times New Roman", serif;
    font-weight: 700;
    font-size: 35px;
    line-height: 42px;
    color: var(--paper);
  }
  .brand {
    position: absolute;
    left: 0;
    width: 812px;
    font-family: "Great Vibes", cursive;
    color: var(--navy);
    font-weight: 400;
    line-height: 1;
    text-align: center;
  }
  .brand--first { top: 495px; font-size: 112px; padding-left: 10px; }
  .brand--second { top: 650px; font-size: 118px; padding-left: 80px; }
  .blend-name {
    position: absolute;
    top: 808px;
    left: 0;
    width: 812px;
    padding-left: 20px;
    text-align: center;
    font-weight: 700;
    font-size: 30px;
    color: var(--ink);
  }
  .tagline {
    position: absolute;
    top: 1045px;
    left: 350px;
    width: 400px;
    text-align: center;
    color: var(--paper);
    font-size: 33px;
    line-height: 45px;
  }
  .volume {
    position: absolute;
    top: 1150px;
    left: 350px;
    width: 400px;
    text-align: center;
    color: var(--paper);
    font-size: 17px;
    font-weight: 700;
  }
</style>
</head>
<body>
<main class="label">
  <svg class="label__art" width="812" height="1200" viewBox="0 0 812 1200">
    <defs>
      <linearGradient id="silver" x1="0" y1="0" x2="1" y2="0">
        <stop offset="0" stop-color="var(--silver-dark)"/>
        <stop offset="0.35" stop-color="var(--silver-light)"/>
        <stop offset="0.7" stop-color="var(--silver-mid)"/>
        <stop offset="1" stop-color="var(--silver-light)"/>
      </linearGradient>
      <linearGradient id="dots" x1="0" y1="0" x2="0" y2="1">
        <stop offset="0" stop-color="var(--dot-green)"/>
        <stop offset="0.14" stop-color="var(--dot-blue)"/>
        <stop offset="0.27" stop-color="var(--dot-red)"/>
        <stop offset="0.38" stop-color="var(--dot-orange)"/>
        <stop offset="0.5" stop-color="var(--dot-yellow)"/>
        <stop offset="0.62" stop-color="var(--dot-orange)"/>
        <stop offset="0.73" stop-color="var(--dot-red)"/>
        <stop offset="0.86" stop-color="var(--dot-blue)"/>
        <stop offset="1" stop-color="var(--dot-green)"/>
      </linearGradient>
    </defs>

    <path class="body-panel" d="M30 0 L812 0 L812 1200 L215 1200 C225 900 240 700 215 520 C190 330 110 150 30 0 Z" fill="url(#silver)"/>
    <rect class="edge-strip" x="785" y="0" width="27" height="860" fill="var(--paper)"/>

    <rect class="dot-band" x="20" y="8" width="778" height="272" fill="url(#dots)" opacity="0.85"
          role="img" aria-label="Columns of bright green, blue, red, orange and yellow dots"/>

    <circle class="badge-circle" cx="400" cy="305" r="140" fill="var(--badge-blue)"/>

    <path class="base-wave" d="M215 1190 C270 1000 520 940 812 800 L812 1190 Z" fill="var(--wave-blue)"/>
    <path class="base-wave-highlight" d="M215 1190 C280 1010 520 950 812 800 L812 830 C540 960 300 1030 240 1190 Z" fill="var(--paper)" opacity="0.35"/>

    <rect class="butterfly" x="540" y="858" width="165" height="150" rx="50" fill="var(--paper)"
          role="img" aria-label="White butterfly silhouette"/>
  </svg>

  <p class="badge-text">Massage Oil<br>Since 1970</p>

  <h1 class="brand brand--first">Bramblewick</h1>
  <p class="brand brand--second">Acres</p>

  <h2 class="blend-name">Unwinding Mix</h2>

  <p class="tagline">20 Years of<br>Natural Skin Care</p>
  <p class="volume">250ml.</p>
</main>
</body>
</html>
```